Bitcoin Trading Bot Startup needs new Website design for product relaunch

Our startup develops an automated Bitcoin trading bot. It's a Crestline extension which monitors the bitcoin markets and triggeres trades accordingly.

We are about to launch a new generation of our bot and need a new design of our website (http://plumvane.com). The bot was named "Marlow Kit" so something orange- or yellowish might make sense, but it's not a hard requirement. The design should be lean and simple.

We want to have the following elements on that page:
- a section on the top with one (or a few) screenshot(s) and a very brief description what our product is
- a table with the different subscription plans we offer (see attachments for the current implementation). When a visitor selects a plan there have to be two differen payment methods offered (quickpurse and bitcoin payment) which ask for different information
- A section which briefly highlights the 3-4 key attributes of the product (safe, versatile, (buttery) smooth (in terms of usability)). There could be links to other pages or an overlay/popup for each of those attributes with a more detailed description
- A list of features
- A testimonials section

There'll be bonus points if you also design a page for the bitcoin payment instructions (see attachment 5).

• No Flash please

```html
<!DOCTYPE html>
<html lang="en">
<head>
<meta charset="utf-8">
<title>Marlow Kit – Automated Bitcoin Trading Bot</title>
<link href="https://fonts.googleapis.com/css2?family=Glegoo:wght@400;700&display=swap" rel="stylesheet">
<style>
  :root {
    --bg: #fecf3a;
    --bg-glow: #fbf08a;
    --ink: #111111;
    --ink-soft: #3d3d3d;
    --heading: #4a4a4a;
    --nav-active: #e1b92c;
    --button: #454545;
    --button-text: #f6cd3d;
    --choose-text: #f2c84a;
    --highlight-col: #fbdd4c;
    --rule: #5a5a5a;
    --mascot-a: #e0b928;
    --mascot-b: #f3d23d;
    --badge: #d8d8d8;
    --white: #ffffff;
  }
  * { margin: 0; padding: 0; box-sizing: border-box; }
  html, body { width: 1200px; height: 1000px; overflow: hidden; }
  body {
    position: relative;
    font-family: "Glegoo", Georgia, serif;
    color: var(--ink);
    background: radial-gradient(circle at 590px 330px, var(--bg-glow) 0, #fde462 120px, var(--bg) 430px);
  }
  .brand { position: absolute; right: 786px; top: 108px; text-align: right; }
  .brand-name { font-size: 42px; font-weight: 700; line-height: 1.1; }
  .brand-tagline { font-size: 12.5px; margin-top: -2px; }

  .main-nav { position: absolute; right: 786px; top: 190px; text-align: right; list-style: none; }
  .main-nav li { margin-bottom: 6px; }
  .main-nav a {
    display: inline-block; font-size: 19px; color: var(--ink);
    text-decoration: none; padding: 0 6px; line-height: 30px; border-radius: 3px;
  }
  .main-nav a.is-active { background: var(--nav-active); color: var(--ink-soft); }

  .payment-badges { position: absolute; left: 194px; top: 405px; display: flex; gap: 8px; }
  .badge-cards { width: 67px; height: 49px; background: var(--white); border: 1px solid #ccc; }
  .badge-coin { width: 138px; height: 51px; background: var(--badge); border-radius: 8px; border: 1px solid #bbb; }

  .testimonial { position: absolute; left: 146px; top: 488px; width: 268px; font-size: 12px; line-height: 14.5px; }
  .testimonial blockquote { text-align: center; }
  .testimonial cite { display: block; text-align: right; font-style: normal; font-size: 10.5px; margin-top: 5px; padding-right: 4px; }

  .mascot {
    position: absolute; left: 470px; top: 132px; width: 214px; height: 340px; border-radius: 10px;
    background: linear-gradient(90deg, var(--mascot-a) 0, var(--mascot-a) 75%, var(--mascot-b) 100%);
  }

  .hero-copy { position: absolute; left: 680px; top: 172px; width: 358px; text-align: center; }
  .extension-icon { display: block; margin: 0 auto; width: 86px; height: 100px; }
  .hero-title { font-size: 31px; font-weight: 400; line-height: 1; margin-top: -2px; white-space: nowrap; }
  .hero-sub { font-size: 14px; line-height: 17px; width: 300px; margin: 0 auto; }
  .cta {
    display: block; width: 251px; height: 45px; margin: 31px auto 0; border-radius: 23px;
    background: var(--button); color: var(--button-text); font-size: 24px; font-weight: 700;
    line-height: 45px; text-decoration: none;
  }

  .slider-dots { position: absolute; left: 703px; top: 507px; display: flex; gap: 28px; list-style: none; }
  .slider-dots li { width: 11px; height: 11px; background: var(--white); }

  .section-title { position: absolute; left: 453px; font-size: 19px; font-weight: 700; color: var(--heading); }
  .features-title { top: 546px; }
  .pricing-title { top: 767px; }

  .feature-list { position: absolute; list-style: none; font-size: 12px; line-height: 14.3px; }
  .feature-list li { position: relative; padding-left: 13px; }
  .feature-list li::before {
    content: ""; position: absolute; left: 0; top: 4px; width: 6px; height: 6px;
    border-radius: 50%; background: var(--ink);
  }
  .fl-a { left: 449px; top: 585px; width: 280px; }
  .fl-b { left: 449px; top: 686px; width: 280px; }
  .fl-c { left: 740px; top: 584px; width: 300px; }
  .fl-d { left: 740px; top: 685px; width: 300px; }

  .pricing { position: absolute; left: 462px; top: 815px; width: 553px; height: 185px; }
  .pricing .col-highlight { position: absolute; left: 409px; top: 0; width: 127px; height: 185px; background: var(--highlight-col); }
  .pricing .col-rule { position: absolute; left: 138px; top: 0; width: 1px; height: 185px; background: var(--rule); }
  .pricing table { position: relative; width: 553px; border-collapse: collapse; table-layout: fixed; font-size: 12px; }
  .pricing th, .pricing td { text-align: center; font-weight: 400; }
  .pricing thead th { height: 31px; font-weight: 700; border-bottom: 1px solid var(--rule); }
  .pricing tbody td { height: 37.5px; }
  .pricing tbody tr:first-child td { padding-top: 6px; height: 43px; }
  .pricing .row-label { text-align: left; padding-left: 26px; font-weight: 700; }
  .pricing .c1 { width: 138px; }
  .pricing .c2 { width: 137px; }
  .pricing .c3 { width: 134px; }
  .pricing .c4 { width: 127px; }
  .pricing .c5 { width: 17px; }
  .choose {
    display: inline-block; width: 95px; height: 31px; line-height: 31px; background: var(--button);
    color: var(--choose-text); font-size: 13px; border-radius: 2px; text-decoration: none;
  }
  .pricing .actions td { height: 40px; vertical-align: top; }
</style>
</head>
<body>
  <header class="brand">
    <div class="brand-name">Marlow Kit</div>
    <div class="brand-tagline">An automated Bitcoin trading bot</div>
  </header>

  <nav>
    <ul class="main-nav">
      <li><a href="http://plumvane.com" class="is-active">Home</a></li>
      <li><a href="#features">Features</a></li>
      <li><a href="#pricing">Plans &amp; Pricing</a></li>
      <li><a href="#testimonials">Testimonials</a></li>
      <li><a href="#contact">Contact Us</a></li>
    </ul>
  </nav>

  <div class="payment-badges" aria-label="Accepted payments: quickpurse and bitcoin">
    <div class="badge-cards"></div>
    <div class="badge-coin"></div>
  </div>

  <aside class="testimonial" id="testimonials">
    <blockquote>"And i have to say they do live up to their support claims. They are very prompt in there response and really helpful. After i reported a bug they released a update within 24 hours."</blockquote>
    <cite>- quillan, coinchatter.org</cite>
  </aside>

  <div class="mascot" role="img" aria-label="Illustration of the Marlow Kit mascot, a friendly butter block character"></div>

  <section class="hero-copy">
    <svg class="extension-icon" role="img" aria-label="Browser extension icon" viewBox="0 0 86 100">
      <rect x="4" y="10" width="78" height="72" rx="4" fill="#c4c4c4"/>
      <ellipse cx="43" cy="96" rx="42" ry="4" fill="#3a3a3a" opacity="0.7"/>
    </svg>
    <h1 class="hero-title">a Crestline extension</h1>
    <p class="hero-sub">which monitors the bitcoin markets and triggeres trades accordingly.</p>
    <a class="cta" href="#pricing">Butter Up!</a>
  </section>

  <ul class="slider-dots" aria-label="Slides">
    <li></li><li></li><li></li><li></li>
  </ul>

  <h2 class="section-title features-title" id="features">Features</h2>
  <ul class="feature-list fl-a">
    <li>USD or EUR trading</li>
    <li>Fully customizable trading strategy</li>
    <li>You can set different trading windows,<br>1 minute, 15 minutes, 30 minutes,<br>45 minutes and 1 hour.</li>
  </ul>
  <ul class="feature-list fl-b">
    <li>Fully automated EMA based trading engine</li>
    <li>Trailing Stop Loss orders</li>
    <li>Mail notifications on imminent orders</li>
    <li>Option to temporarily disable trading</li>
  </ul>
  <ul class="feature-list fl-c">
    <li>You can set two different thresholds for buy and sell commands. You will be notified when the EMA value passes threshold 1 but the bot will only trade after the EMA value has passed threshold 2. Thats 2 threshold for "buy" and 2 thresholds for "sell" that you can set.</li>
  </ul>
  <ul class="feature-list fl-d">
    <li>The bot now displays a beautiful graph to show you the trend</li>
    <li>There is an arrow on the display showing whether the trend is going up or down.</li>
    <li>Robust codebase based on Larkjs</li>
  </ul>

  <h2 class="section-title pricing-title" id="pricing">Plans &amp; Pricing</h2>
  <div class="pricing">
    <div class="col-highlight"></div>
    <div class="col-rule"></div>
    <table>
      <colgroup><col class="c1"><col class="c2"><col class="c3"><col class="c4"><col class="c5"></colgroup>
      <thead>
        <tr><th class="row-label">Subscription</th><th>3 months</th><th>6 months</th><th>12 months</th><th></th></tr>
      </thead>
      <tbody>
        <tr><td class="row-label">Bot Price</td><td>$ 59.99</td><td>$ 59.99</td><td>$ 59.99</td><td></td></tr>
        <tr><td class="row-label">Price/month</td><td>$ 9.99</td><td>$ 8.99</td><td>$ 6.99</td><td></td></tr>
        <tr><td class="row-label">Total</td><td>$ 89.96</td><td>$ 113.93</td><td>$ 143.87</td><td></td></tr>
        <tr class="actions"><td></td><td><a class="choose" href="#">choose</a></td><td><a class="choose" href="#">choose</a></td><td><a class="choose" href="#">choose</a></td><td></td></tr>
      </tbody>
    </table>
  </div>
</body>
</html>
```